Determining number of boxes of planks of flooring for a room

Need a creative design of an infographic of a room with instructions on how to measure the room and use this measurement to determine how much flooring to order.
The floor planks come in boxes and each box has 36 planks. Each box covers 5 metre squared in total.
The intent of the infographic is to help inform the customer how many boxes they need to order for their room.
The infographic should match the style of flooring being sold (image provided) and the logo for the company (image provided).
A crude sketch of instructions to measure a room and determine the number of boxes is provided in a document attached with this brief. Need improvement to the steps mentioned in this document on the infographic created.

```html
<!DOCTYPE html>
<html lang="en">
<head>
<meta charset="utf-8">
<title>How To Work Out Room Size and Floor Packs</title>
<link rel="stylesheet" href="https://fonts.googleapis.com/css2?family=Montserrat:ital,wght@0,400;0,500;0,600;0,700;0,900;1,400;1,500&display=swap">
<style>
  :root {
    --bg: #e4e4e4;
    --plank-line: #c2c2c2;
    --brown-dark: #5e5444;
    --brown-mid: #7a6446;
    --tape-yellow: #e8e86a;
    --ink: #2a2a2a;
    --white: #ffffff;
    --red: #e52421;
    --green: #3a8a3a;
    --blue: #1a5aa8;
    --wall: #8fa898;
    --floor: #c4925a;
  }
  * { box-sizing: border-box; margin: 0; padding: 0; }
  html, body { width: 1200px; height: 849px; overflow: hidden; background: var(--bg); }
  .infographic {
    position: relative; width: 1200px; height: 849px; overflow: hidden;
    font-family: "Montserrat", sans-serif; color: var(--ink);
    background: linear-gradient(180deg, #e8e8e8 0%, #dedede 100%);
  }
  .planks { position: absolute; inset: 0; }
  .tape-band {
    position: absolute; left: 326px; top: 48px; width: 386px; height: 48px;
    border-radius: 0 6px 6px 0;
    background: linear-gradient(90deg, var(--tape-yellow) 0%, var(--tape-yellow) 92%, #4a4a4a 92%, #4a4a4a 100%);
  }
  .title-how {
    position: absolute; left: 52px; top: 36px;
    font-size: 70px; font-weight: 900; color: var(--brown-dark);
    letter-spacing: -2px; line-height: 1;
    text-shadow: 2px 3px 4px rgba(0,0,0,0.25);
  }
  .title-sub {
    position: absolute; left: 55px; top: 112px;
    font-size: 42px; font-weight: 600; color: var(--white);
    -webkit-text-stroke: 1.5px var(--brown-dark);
    text-shadow: 2px 3px 4px rgba(0,0,0,0.3);
    letter-spacing: 0.3px;
  }
  .brand { position: absolute; left: 910px; top: 44px; display: flex; align-items: center; gap: 10px; }
  .brand-mark { width: 40px; height: 40px; background: var(--brown-dark); }
  .brand-name { font-size: 31px; font-weight: 500; color: var(--brown-dark); letter-spacing: 2px; line-height: 1; }
  .brand-tagline { font-size: 8px; font-weight: 500; color: var(--brown-dark); letter-spacing: 3.2px; margin-top: 3px; }
  .step-head {
    position: absolute; left: 53px; width: 492px; height: 45px;
    display: flex; background: var(--brown-dark);
    box-shadow: 2px 3px 5px rgba(0,0,0,0.3);
    color: var(--white); font-size: 27px; font-weight: 500;
  }
  .step-head .num { width: 45px; background: var(--brown-mid); display: flex; align-items: center; justify-content: center; }
  .step-head .label { flex: 1; display: flex; align-items: center; justify-content: center; }
  .step-one { top: 204px; }
  .step-two { top: 481px; }
  .copy { position: absolute; left: 54px; font-size: 22px; line-height: 27.5px; font-weight: 400; }
  .note { position: absolute; left: 53px; font-size: 19px; line-height: 23.5px; font-style: italic; font-weight: 500; }
  .var { font-weight: 700; }
  .var-a, .var-b { color: var(--red); }
  .var-c { color: var(--green); }
  .var-d { color: var(--blue); }
  .room-illustration {
    position: absolute; left: 635px; top: 267px; width: 530px; height: 459px;
    background: linear-gradient(180deg, var(--wall) 0%, var(--wall) 45%, var(--floor) 62%, #b8844e 100%);
  }
</style>
</head>
<body>
<main class="infographic">
  <svg class="planks" width="1200" height="849" aria-hidden="true">
    <g stroke="var(--plank-line)" stroke-width="2">
      <line x1="0" y1="27" x2="1200" y2="27"/><line x1="0" y1="107" x2="1200" y2="107"/>
      <line x1="0" y1="186" x2="1200" y2="186"/><line x1="0" y1="264" x2="1200" y2="264"/>
      <line x1="0" y1="344" x2="1200" y2="344"/><line x1="0" y1="422" x2="1200" y2="422"/>
      <line x1="0" y1="501" x2="1200" y2="501"/><line x1="0" y1="580" x2="1200" y2="580"/>
      <line x1="0" y1="660" x2="1200" y2="660"/><line x1="0" y1="739" x2="1200" y2="739"/>
      <line x1="0" y1="818" x2="1200" y2="818"/>
    </g>
  </svg>

  <div class="tape-band" role="img" aria-label="Illustration of an extended tape measure running from the title"></div>
  <h1 class="title-how">HOW TO</h1>
  <h2 class="title-sub">Work to Out Room Size and Floor Packs</h2>

  <div class="brand">
    <span class="brand-mark"></span>
    <div>
      <div class="brand-name">VERDANO</div>
      <div class="brand-tagline">PREMIUM FLOORS AND TILES</div>
    </div>
  </div>

  <div class="step-head step-one"><span class="num">1</span><span class="label">Measure Room Dimensions</span></div>
  <p class="copy" style="top:280px">Use room length <span class="var var-a">A</span> multiply room width <span class="var var-b">B</span><br>
    <span class="var var-a">A</span> x <span class="var var-b">B</span> = <span class="var var-c">C</span>, In this case you will have room size <span class="var var-c">C</span></p>
  <p class="note" style="top:355px">*(If your room is not a square shape, please do a<br>simple drawing and send it to us. We will be able to<br>work it out for you)</p>

  <div class="step-head step-two"><span class="num">2</span><span class="label">Work Out Pack Numbers</span></div>
  <p class="copy" style="top:558px">Use room size <span class="var var-c">C</span> divided by 5<br>
    <span class="var var-c">C</span>/5 = <span class="var var-d">D</span>, <span class="var var-d">D</span> is number of packs of floor you need to<br>cover this area</p>
  <p class="copy" style="top:668px">If <span class="var var-d">D</span> has decimal points, please always round up to<br>the next integer, e.g.<br>
    if <span class="var var-d">D</span> = 3.1, then <span class="var var-d">D</span> needs to be 4 or<br>
    if <span class="var var-d">D</span> = 3.8, <span class="var var-d">D</span> still needs to be 4</p>

  <div class="room-illustration" role="img" aria-label="Isometric illustration of a furnished bedroom with a wooden floor, with arrows marking room length A and room width B"></div>
</main>
</body>
</html>
```